Business Cards and Letter Head for Mini Excavator Hire Business
Business Cards and Letter Heads
Stone-Willow
Dermot Halvey
Mini Excavator Specialist
41 Morlena Court
East Callowmere Vic 3184
dermot@plovtrek.com.au
plovtrek.com.au
Would like the front and back of the business card to be black (C:75 M:68 K:90).
Font: Helvetica CondensedBlack
• BRX Mini Hydraulic Excavator Hire
• From $297.00 per day including GST
• Cheaper rates for weekly or monthly hire
• Supplied complete with trailer & 3 buckets
• Auger attachments available
Book yours today!
Information regarding the business card design.
Logo design attached.

```html
<!DOCTYPE html>
<html lang="en">
<head>
<meta charset="utf-8">
<title>Plovtrek Hire – Business Card</title>
<link rel="stylesheet" href="https://fonts.googleapis.com/css2?family=Roboto+Condensed:wght@400;700;900&display=swap">
<style>
  :root {
    --card-black: #0f1010;
    --hire-yellow: #f3e500;
    --text-white: #f4f4f4;
    --text-grey: #cfcfcf;
    --page-bg: #e6e6e4;
  }
  * { box-sizing: border-box; margin: 0; padding: 0; }
  html, body { width: 1200px; height: 720px; overflow: hidden; }
  body {
    background: var(--page-bg);
    font-family: "Roboto Condensed", "Arial Narrow", sans-serif;
    display: flex;
    align-items: center;
    justify-content: center;
    gap: 40px;
  }
  .card {
    position: relative;
    width: 560px;
    height: 320px;
    background: var(--card-black);
    border-radius: 3px;
    box-shadow: 0 6px 18px rgba(0,0,0,.25);
    overflow: hidden;
    color: var(--text-white);
  }

  /* Brand lockup */
  .brand { display: flex; align-items: center; gap: 12px; }
  .brand-square { width: 48px; height: 48px; background: var(--hire-yellow); flex: none; }
  .brand-name {
    font-weight: 900;
    font-size: 42px;
    line-height: 1;
    color: var(--hire-yellow);
    text-transform: uppercase;
    letter-spacing: .5px;
    white-space: nowrap;
  }

  /* Front */
  .card-front .side-bar {
    position: absolute; left: 0; top: 0; bottom: 0; width: 20px;
    background: var(--hire-yellow);
  }
  .card-front .brand-band {
    position: absolute; left: 0; top: 30px; width: 92px; height: 68px;
    background: var(--hire-yellow);
  }
  .card-front .brand {
    position: absolute; left: 32px; top: 40px;
  }
  .card-front .brand-square { background: var(--card-black); }
  .card-front .brand-name { margin-left: 14px; }
  .holder {
    position: absolute; left: 44px; top: 122px;
    font-size: 15px; white-space: nowrap;
  }
  .holder-name {
    font-weight: 700; font-size: 20px; color: var(--hire-yellow);
    text-decoration: underline; text-underline-offset: 3px;
  }
  .holder-role { color: var(--text-white); }
  .contact-list {
    position: absolute; left: 44px; top: 160px;
    list-style: none;
    font-size: 15px; line-height: 23px;
  }
  .contact-list li { display: flex; align-items: center; gap: 10px; }
  .contact-list svg { width: 13px; height: 13px; fill: var(--hire-yellow); flex: none; }
  .divider {
    position: absolute; left: 262px; top: 162px; width: 1px; height: 110px;
    background: var(--text-grey);
  }
  .address {
    position: absolute; left: 278px; top: 160px;
    font-style: normal; font-size: 15px; line-height: 23px;
  }

  /* Back */
  .card-back .brand {
    position: absolute; left: 0; right: 0; top: 34px; justify-content: center;
  }
  .card-back .brand-name { font-size: 50px; }
  .card-back .brand-square { width: 56px; height: 56px; }
  .stripe-band {
    position: absolute; left: 0; right: 0; top: 118px; height: 66px;
    background: linear-gradient(90deg, #d9cd00, var(--hire-yellow) 50%, #d9cd00);
  }
  .offer-list {
    position: absolute; left: 30px; right: 30px; top: 198px;
    list-style: none;
    display: flex; flex-wrap: wrap; justify-content: center;
    column-gap: 14px; row-gap: 2px;
    font-size: 13.5px; line-height: 18px; color: var(--text-white);
  }
  .offer-list li { white-space: nowrap; }
  .offer-list li::before { content: "• "; color: var(--hire-yellow); }
  .cta {
    position: absolute; left: 0; right: 0; top: 266px;
    text-align: center; font-weight: 700; font-size: 15px; line-height: 18px;
  }
  .web {
    position: absolute; left: 0; right: 0; top: 290px;
    text-align: center; font-size: 14px; line-height: 18px; color: var(--hire-yellow);
  }
</style>
</head>
<body>

  <section class="card card-front" aria-label="Business card front">
    <div class="side-bar"></div>
    <div class="brand-band"></div>
    <div class="brand">
      <span class="brand-square"></span>
      <span class="brand-name">Plovtrek Hire</span>
    </div>

    <p class="holder"><span class="holder-name">Dermot Halvey</span><span class="holder-role">, Mini Excavator Specialist</span></p>

    <ul class="contact-list">
      <li>
        <svg viewBox="0 0 24 24" aria-hidden="true"><path d="M6.6 10.8a15 15 0 0 0 6.6 6.6l2.2-2.2c.3-.3.7-.4 1-.2 1.1.4 2.3.6 3.6.6.6 0 1 .4 1 1V20c0 .6-.4 1-1 1A17 17 0 0 1 3 4c0-.6.4-1 1-1h3.5c.6 0 1 .4 1 1 0 1.3.2 2.5.6 3.6.1.3 0 .7-.2 1z"/></svg>
        1300 48 27 60
      </li>
      <li>
        <svg viewBox="0 0 24 24" aria-hidden="true"><path d="M7 1h10a2 2 0 0 1 2 2v18a2 2 0 0 1-2 2H7a2 2 0 0 1-2-2V3a2 2 0 0 1 2-2zm0 3v14h10V4z"/></svg>
        0412 555 019
      </li>
      <li>
        <svg viewBox="0 0 24 24" aria-hidden="true"><path d="M6 2h10l2 2v5h2a2 2 0 0 1 2 2v8h-4v3H6v-3H2v-8a2 2 0 0 1 2-2h2zm2 2v5h8V5h-1V4zm0 12v4h8v-4z"/></svg>
        03 9555 0147
      </li>
      <li>
        <svg viewBox="0 0 24 24" aria-hidden="true"><path d="M2 4h20v16H2zm2 2v.5l8 5 8-5V6zm0 3v9h16V9l-8 5z"/></svg>
        dermot@plovtrek.com.au
      </li>
      <li>
        <svg viewBox="0 0 24 24" aria-hidden="true"><path d="M12 2a10 10 0 1 0 0 20 10 10 0 0 0 0-20zm0 2c.9 1 1.7 2.6 2.1 5H9.9C10.3 6.6 11.1 5 12 4zM4.3 11h3.5c0 .7 0 1.4.1 2H4.3a8 8 0 0 1 0-2zm5.6 0h4.2a13 13 0 0 1 0 2H9.9a13 13 0 0 1 0-2zm6.3 0h3.5a8 8 0 0 1 0 2h-3.5l.1-2zM9.9 15h4.2c-.4 2.4-1.2 4-2.1 5-.9-1-1.7-2.6-2.1-5z"/></svg>
        www.plovtrek.com.au
      </li>
    </ul>

    <div class="divider"></div>
    <address class="address">
      41 Morlena Court<br>
      East Callowmere Vic 3184
    </address>
  </section>

  <section class="card card-back" aria-label="Business card back">
    <div class="brand">
      <span class="brand-square"></span>
      <span class="brand-name">Plovtrek Hire</span>
    </div>

    <div class="stripe-band" role="img" aria-label="Yellow and black diagonal hazard stripe band"></div>

    <ul class="offer-list">
      <li>BRX Mini Hydraulic Excavator Hire</li>
      <li>From $297.00 per day including GST</li>
      <li>Cheaper rates for weekly or monthly hire</li>
      <li>Supplied complete with trailer &amp; 3 buckets</li>
      <li>Auger attachments available</li>
    </ul>
    <p class="cta">Book yours today!</p>
    <p class="web">www.plovtrek.com.au</p>
  </section>

</body>
</html>
```